Nestlyo Business Card Project showing the logo and a vonka image on the rear

Design a whacky but professional business card, the logo is for the front and the Vonka image is for the rear. Happy to consider other open source Vonka Images if the designer wants to select one from the web. Nestlyo is a competitor to KPX.com.au and Plotfield.com.au and is based around every property in Australia

Business

Name, Title, Email, Web, Phone Number

• avenir

• Image on Back logo on front
• Happy to consider other images on rear, preftably Oscar Vonka. Image supplied I own, we can use open source other Vonka Images

```html
<!DOCTYPE html>
<html lang="en">
<head>
<meta charset="utf-8">
<title>Nestlyo Business Card</title>
<link rel="stylesheet" href="https://fonts.googleapis.com/css2?family=Montserrat:wght@400;600;700;800&display=swap">
<style>
  :root {
    --backdrop: #1c1c1e;
    --brand-orange: #f68b1f;
    --ink: #161616;
    --paper: #ffffff;
    --sky-blue: #2f7fd9;
    --sky-deep: #2a4fc0;
    --city-warm: #e8682a;
    --city-yellow: #f2c21b;
  }
  * { margin: 0; padding: 0; box-sizing: border-box; }
  html, body { width: 1200px; height: 900px; overflow: hidden; }
  body {
    background: var(--backdrop);
    font-family: "Montserrat", sans-serif;
    display: flex;
    flex-direction: column;
    align-items: center;
    justify-content: center;
    gap: 40px;
  }
  .card {
    width: 700px;
    height: 400px;
    position: relative;
    overflow: hidden;
    box-shadow: 0 12px 30px rgba(0,0,0,.5);
  }
  .card-front { background: var(--brand-orange); color: var(--ink); }
  .front-corner { position: absolute; inset: 0; }
  .brand {
    position: absolute;
    left: 56px;
    top: 52px;
    display: flex;
    align-items: center;
    gap: 16px;
  }
  .brand-square {
    width: 40px; height: 40px;
    background: var(--paper);
  }
  .brand-name {
    font-weight: 800;
    font-size: 54px;
    letter-spacing: 1px;
  }
  .contact {
    position: absolute;
    left: 56px;
    top: 180px;
  }
  .contact-name {
    font-weight: 700;
    font-size: 24px;
    letter-spacing: 1px;
    text-transform: uppercase;
  }
  .contact-title { font-size: 20px; margin-top: 2px; }
  .contact-rule {
    width: 18px; height: 2px;
    background: var(--ink);
    margin: 12px 0 10px;
  }
  .contact-list { list-style: none; font-size: 20px; line-height: 1.35; }
  .contact-list li { display: flex; align-items: center; gap: 8px; }
  .contact-list svg { width: 14px; height: 14px; flex: none; }
  .card-back .city-art {
    position: absolute; inset: 0;
    background: linear-gradient(180deg, var(--sky-blue) 0%, var(--sky-deep) 42%, var(--city-warm) 70%, var(--city-yellow) 100%);
  }
</style>
</head>
<body>
  <section class="card card-front" aria-label="Card front">
    <svg class="front-corner" viewBox="0 0 700 400" preserveAspectRatio="none" aria-hidden="true">
      <polygon points="560,0 700,0 700,220" fill="var(--paper)"/>
    </svg>
    <div class="brand">
      <span class="brand-square"></span>
      <span class="brand-name">Nestlyo</span>
    </div>
    <div class="contact">
      <p class="contact-name">Darren Cole</p>
      <p class="contact-title">Director</p>
      <div class="contact-rule"></div>
      <ul class="contact-list">
        <li>
          <svg viewBox="0 0 16 16"><path d="M4 1l3 3-2 2c1 2 3 4 5 5l2-2 3 3-2 3C7 14 2 9 1 3z" fill="var(--ink)"/></svg>
          432-555-0148
        </li>
        <li>
          <svg viewBox="0 0 16 16"><rect x="1" y="3" width="14" height="10" fill="none" stroke="var(--ink)" stroke-width="1.5"/><path d="M1 3l7 6 7-6" fill="none" stroke="var(--ink)" stroke-width="1.5"/></svg>
          info@nestlyo.com.au
        </li>
        <li>
          <svg viewBox="0 0 16 16"><circle cx="8" cy="8" r="6.5" fill="none" stroke="var(--ink)" stroke-width="1.5"/><path d="M1.5 8h13M8 1.5c-3 3-3 10 0 13M8 1.5c3 3 3 10 0 13" fill="none" stroke="var(--ink)" stroke-width="1.2"/></svg>
          www.nestlyo.com.au
        </li>
      </ul>
    </div>
  </section>

  <section class="card card-back" aria-label="Card back">
    <div class="city-art" role="img" aria-label="Colourful pop-art illustration of a cheerful city skyline with stars, a moon and clouds by Oscar Vonka"></div>
  </section>
</body>
</html>
```